Clinician Harbor Collective

I am a financial planner whose client's are physicians and dentists. As physicians, there is very little time for them to do research on numerous aspects of their business and personal lives. I am looking to build a website that is a 1 stop shop for many of the services/resources they may need. It will be my job to screen the resources/advertisers and place competent people/business's that I know and have a track record on. there will ultimately be 10 or 12 ish areas that I would like to provide resources in:
disability insurance
life insurance
retirement planning
student loan advisors
employment contract and business formation attorneys
accountants
real estate agents
physician mortgages
personal loans
malpractice insurance
physician recruiters
maybe 2 other areas which I have yet to figure out.....
I would like each of these options to be able to be clicked on and a page will open up with the 1 or 2 or 3 or 4 people/business's that I have picked to represent these areas. I would like each specific person/business to have a click here to contact me link in which an email goes to the person and I am copied on the initial correspondence between the physician and the mortgage broker.... just so I can see some of the correspondence they will be receiving.
nowhere on the site do I want it to say my name. there will be certain disclosures that are needed and other wording but I think this is a good starting point.
here are links to two websites with the same general concept. please keep in mind that I want my website to be more on the simple side.
http://www.vantorelmedlink.example/index.html
http://bluestethwealth.example/
Industry/Entity Type
Financial

```html
<!DOCTYPE html>
<html lang="en">
<head>
<meta charset="utf-8">
<title>Clinician Harbor Collective</title>
<link href="https://fonts.googleapis.com/css2?family=Arimo:ital,wght@0,400;0,700;1,400&display=swap" rel="stylesheet">
<style>
:root{
  --page-bg:#0b6690;
  --white:#ffffff;
  --brand:#1a6e92;
  --heading:#1267b8;
  --text:#222222;
  --muted:#777777;
  --rule:#dddddd;
  --nav-top:#f4f4f4;
  --nav-bottom:#d6d6d6;
  --nav-border:#c4c4c4;
  --red:#e8493a;
  --green:#22bb5e;
  --blue:#3d8ecd;
  --footer:#262626;
  --footer-text:#b8b8b8;
  --button:#1466b8;
}
*{margin:0;padding:0;box-sizing:border-box}
html,body{width:1126px;height:1200px;overflow:hidden}
body{background:var(--page-bg);font-family:"Arimo",Arial,sans-serif;color:var(--text);position:relative}
.sheet{position:absolute;left:151px;top:0;width:823px;height:1200px;background:var(--white)}
.abs{position:absolute}

/* header */
.brand{left:11px;top:38px;display:flex;align-items:center;gap:10px}
.brand-dot{width:14px;height:14px;border-radius:50%;background:var(--brand)}
.brand-name{font-size:21px;font-weight:700;color:var(--brand);letter-spacing:.2px}
.call{right:13px;top:40px;display:flex;align-items:center;gap:8px}
.call-label{font-size:10px;color:#888}
.call-number{font-size:14px;color:var(--brand)}

/* nav */
.nav{left:11px;top:102px;width:805px;height:38px;display:flex;border:1px solid var(--nav-border);background:linear-gradient(var(--nav-top),var(--nav-bottom))}
.nav a{display:flex;align-items:center;justify-content:center;font-size:12px;color:#222;text-decoration:none;border-right:1px solid var(--nav-border)}
.nav a:last-child{border-right:0}

/* hero */
.hero{left:11px;top:140px;width:805px;height:322px;background:linear-gradient(90deg,#e8eef4 0%,#c9d6e6 35%,#eef1f4 60%,#d9c7bd 85%,#b49d8f 100%)}
.hero-text{left:412px;top:126px;width:360px}
.hero-text .lead{font-size:19px;font-weight:700;color:var(--brand);letter-spacing:.3px}
.hero-text .rest{font-size:18px;line-height:29px;color:#111;margin-top:4px}
.hero-arrows{right:15px;bottom:12px;display:flex;gap:1px}
.hero-arrows span{width:22px;height:22px;background:#7d7d7d;display:flex;align-items:center;justify-content:center}

.section-title{font-size:14px;color:var(--heading);letter-spacing:.2px}

/* services */
.service{width:184px}
.service-photo{width:184px;height:120px;position:relative}
.service-more{position:absolute;left:0;bottom:0;height:29px;padding:0 16px;background:rgba(60,60,60,.82);color:#fff;font-size:10.5px;display:flex;align-items:center}
.service-name{margin-top:15px;font-size:10.5px;font-weight:700;color:var(--heading)}
.service-desc{margin-top:7px;font-size:10.5px;line-height:19px;color:var(--muted)}

.divider{left:20px;top:730px;width:785px;height:2px;background:var(--rule)}

/* about */
.about-lead{font-size:12.5px;line-height:21px;color:#222}
.about-body{font-size:10.5px;line-height:19px;color:var(--muted)}
.read-more{display:inline-flex;align-items:center;height:25px;padding:0 14px;background:var(--button);color:#fff;font-size:10px;border-radius:3px}

/* posts */
.post-date{font-size:11.5px;color:#999}
.post-date b{font-size:14px;color:#555}
.post-rule{height:1px;background:var(--rule);width:258px}
.post-title{font-size:12px;color:var(--heading)}
.post-body{font-size:10px;line-height:19px;color:var(--muted);width:250px}
.mini-arrows{display:flex;gap:1px}
.mini-arrows span{width:14px;height:13px;background:#c7c7c7;display:flex;align-items:center;justify-content:center}

/* callouts */
.callout{left:583px;width:224px;height:89px;padding:20px 24px;color:#fff}
.callout h3{font-size:11.5px;font-weight:400;letter-spacing:.2px}
.callout p{font-size:10px;font-style:italic;line-height:19px;margin-top:6px}
.callout-red{background:var(--red)}
.callout-green{background:var(--green)}
.callout-blue{background:var(--blue)}

/* footer */
.footer{left:11px;top:1100px;width:805px;height:90px;background:var(--footer)}
.footer-nav{left:27px;top:27px;display:flex;font-size:9px;color:var(--footer-text)}
.footer-nav span.sep{margin:0 18px}
.copyright{left:27px;top:53px;font-size:8.5px;color:var(--footer-text)}
.follow{right:16px;top:34px;display:flex;align-items:center;gap:8px;font-size:7.5px;color:#999}
.follow i{display:block;width:24px;height:24px;border:1px solid #666}
</style>
</head>
<body>
<div class="sheet">

  <header>
    <div class="abs brand">
      <span class="brand-dot"></span>
      <span class="brand-name">Clinician Harbor Collective</span>
    </div>
    <div class="abs call">
      <svg width="38" height="38" viewBox="0 0 38 38" aria-hidden="true">
        <circle cx="19" cy="19" r="17" fill="none" stroke="#1a6e92" stroke-width="2"/>
        <path d="M14 11c-2 2-2 5 0 9s5 7 9 8c2 0 3-1 3-2l-2-3c-1-1-2 0-3 0-2-1-4-4-5-6 0-1 1-2 0-3l-2-3z" fill="#1a6e92"/>
      </svg>
      <div>
        <div class="call-label">CALL US :</div>
        <div class="call-number">( 1250 ) 555 0147</div>
      </div>
    </div>
  </header>

  <nav class="abs nav">
    <a style="width:106px">HOME</a>
    <a style="width:107px">ABOUT US</a>
    <a style="width:117px">SERVICES</a>
    <a style="width:124px">RESOURCES</a>
    <a style="width:119px">FEATURES</a>
    <a style="width:85px">BLOG</a>
    <a style="flex:1">CONTACT US</a>
  </nav>

  <section class="abs hero" role="img" aria-label="Photo of a smiling grey-haired doctor with a stethoscope listening to a patient">
    <div class="abs hero-text">
      <div class="lead">IAM A FINANCIAL PLANNER AND</div>
      <div class="rest">I WILL ADVISE TO PHYSICIANS &amp;<br>DENTISTS.</div>
    </div>
    <div class="abs hero-arrows">
      <span><svg width="8" height="10"><path d="M6 1L2 5l4 4" stroke="#fff" fill="none" stroke-width="1.3"/></svg></span>
      <span><svg width="8" height="10"><path d="M2 1l4 4-4 4" stroke="#fff" fill="none" stroke-width="1.3"/></svg></span>
    </div>
  </section>

  <h2 class="abs section-title" style="left:18px;top:486px">SERVICES</h2>

  <article class="abs service" style="left:17px;top:518px">
    <div class="service-photo" role="img" aria-label="Photo of glasses and a pen on an insurance claim form" style="background:linear-gradient(135deg,#e9edf2,#b9c9da 70%,#8fa7c0)"><span class="service-more">READ MORE</span></div>
    <h3 class="service-name">DISABILITY INSURANCE</h3>
    <p class="service-desc">Lorem Ipsum is simply dummy text of the printing and typesetting...</p>
  </article>
  <article class="abs service" style="left:222px;top:518px">
    <div class="service-photo" role="img" aria-label="Photo of a smiling family of four" style="background:linear-gradient(135deg,#e2d8cc,#c88b7a 50%,#4f86c6)"><span class="service-more">READ MORE</span></div>
    <h3 class="service-name">LIFE INSURANCE</h3>
    <p class="service-desc">Lorem Ipsum is simply dummy text of the printing and typesetting...</p>
  </article>
  <article class="abs service" style="left:427px;top:518px">
    <div class="service-photo" role="img" aria-label="Photo of a happy retired couple" style="background:linear-gradient(135deg,#9fb4c6,#e6d5c3 50%,#c99d6e)"><span class="service-more">READ MORE</span></div>
    <h3 class="service-name">RETIREMENT PLANNING</h3>
    <p class="service-desc">Lorem Ipsum is simply dummy text of the printing and typesetting...</p>
  </article>
  <article class="abs service" style="left:631px;top:518px">
    <div class="service-photo" role="img" aria-label="Photo of students holding books outdoors" style="background:linear-gradient(135deg,#8fae6a,#d8d2c3 50%,#5b6f8c)"><span class="service-more">READ MORE</span></div>
    <h3 class="service-name">STUDENT LOAN ADVISORS</h3>
    <p class="service-desc">Lorem Ipsum is simply dummy text of the printing and typesetting...</p>
  </article>

  <div class="abs divider"></div>

  <section class="abs" style="left:17px;top:759px;width:240px">
    <h2 class="section-title">CLINICIAN HARBOR COLLECTIVE</h2>
    <div role="img" aria-label="Photo of a team of smiling doctors and nurses" style="margin-top:16px;width:238px;height:117px;background:linear-gradient(90deg,#e8eef3,#9ab8d8 45%,#dfe6ee 75%,#f4f6f8)"></div>
    <p class="about-lead" style="margin-top:14px">Lorem Ipsum is simply dummy text of the printing and typesetting industry.</p>
    <p class="about-body" style="margin-top:6px">Lorem Ipsum is simply dummy text of the printing and typesetting industry. Lorem Ipsum has been the industry's standard dummy...</p>
    <span class="read-more" style="margin-top:12px">Read More &raquo;</span>
  </section>

  <section class="abs" style="left:289px;top:759px;width:258px">
    <h2 class="section-title">RECENT POSTS</h2>
    <div class="abs mini-arrows" style="right:0;top:1px">
      <span><svg width="6" height="8"><path d="M5 1L2 4l3 3" stroke="#fff" fill="none"/></svg></span>
      <span><svg width="6" height="8"><path d="M1 1l3 3-3 3" stroke="#fff" fill="none"/></svg></span>
    </div>
    <div class="post-date" style="margin-top:14px"><b>24</b> March</div>
    <div class="post-rule" style="margin-top:11px"></div>
    <div class="post-title" style="margin:15px 0 0 5px">Lorem Ipsum is simply dummy text.</div>
    <p class="post-body" style="margin:9px 0 0 5px">Lorem Ipsum is simply dummy text of the printing and typesetting industry. Lorem Ipsum has been the industry's standard dummy...</p>
    <div class="post-rule" style="margin-top:9px"></div>
    <div class="post-date" style="margin-top:13px"><b>28</b> March</div>
    <div class="post-rule" style="margin-top:11px"></div>
    <div class="post-title" style="margin:15px 0 0 5px">Lorem Ipsum is simply dummy text.</div>
    <p class="post-body" style="margin:9px 0 0 5px">Lorem Ipsum is simply dummy text of the printing and typesetting industry. Lorem Ipsum has been the industry's standard dummy...</p>
  </section>

  <div class="abs callout callout-red" style="top:758px">
    <h3>RESOURCES &amp; ADVERTISERS</h3>
    <p>Lorem Ipsum is simply dummy text of the printing &raquo;</p>
  </div>
  <div class="abs callout callout-green" style="top:859px">
    <h3>FINANCIAL PLANNER</h3>
    <p>Lorem Ipsum is simply dummy text of the printing &raquo;</p>
  </div>
  <div class="abs callout callout-blue" style="top:959px">
    <h3>PHYSICIANS &amp; DENTISTS</h3>
    <p>Lorem Ipsum is simply dummy text of the printing &raquo;</p>
  </div>

  <footer class="abs footer">
    <div class="abs footer-nav">
      <span>HOME</span><span class="sep">|</span><span>ABOUT US</span><span class="sep">|</span><span>SERVICES</span><span class="sep">|</span><span>RESOURCES</span><span class="sep">|</span><span>FEATURES</span><span class="sep">|</span><span>BLOG</span><span class="sep">|</span><span>CONTACT US</span>
    </div>
    <div class="abs copyright">© 2014. CLINICIAN HARBOR COLLECTIVE. ALL RIGHTS RESERVED.</div>
    <div class="abs follow">
      <span>FOLLOW US :</span><i></i><i></i><i></i><i></i>
    </div>
  </footer>

</div>
</body>
</html>
```